" A empresa funciona em um escritório físico, onde os clientes são recebidos para conversar sobre como desejam seu projeto residencial ou comercial. Oferecemos também projetos de decoração, e de instalações, bem como projeto de estrutura. O processo de criação se da tambem pela produção de projetos em 3d. alem da produção do projeto acompanhamos tambem a obra e todo o processo de construção. "

```html
<!DOCTYPE html>
<html lang="pt-BR">
<head>
<meta charset="utf-8">
<title>Marina Lacerda — Cartão de visita</title>
<link rel="stylesheet" href="https://fonts.googleapis.com/css2?family=Questrial&display=swap">
<style>
  :root {
    --backdrop: #e9e8e6;
    --card-grey: #7f8083;
    --text-grey: #6d6e71;
    --icon-grey: #9a9b9e;
    --brand-yellow: #fcd82a;
    --card-white: #ffffff;
  }
  * { box-sizing: border-box; margin: 0; padding: 0; }
  html, body {
    width: 1200px; height: 1200px; overflow: hidden;
    background: var(--backdrop);
    font-family: "Questrial", "Century Gothic", sans-serif;
  }
  .canvas { position: relative; width: 1200px; height: 1200px; }

  /* Front face */
  .card-front {
    position: absolute; left: 200px; top: 96px;
    width: 800px; height: 456px;
    background: var(--card-grey);
    border-radius: 0 228px 0 0;
    box-shadow: 0 12px 30px rgba(0,0,0,.18);
  }
  .front-mark {
    position: absolute; left: 380px; top: 196px;
    display: flex; align-items: center; gap: 22px;
  }
  .front-dot {
    width: 44px; height: 44px; border-radius: 50%;
    background: var(--brand-yellow);
  }
  .front-name {
    color: var(--card-white);
    font-size: 34px; letter-spacing: 2px; line-height: 1;
  }
  .front-tagline {
    margin-top: 8px;
    color: var(--brand-yellow);
    font-size: 15px; letter-spacing: 2.5px;
  }

  /* Back face */
  .card-back {
    position: absolute; left: 200px; top: 642px;
    width: 800px; height: 450px;
    box-shadow: 0 12px 30px rgba(0,0,0,.18);
    border-radius: 210px 0 0 0;
    overflow: hidden;
  }
  .card-back-shape { position: absolute; inset: 0; }
  .back-mark {
    position: absolute; left: 460px; top: 36px; width: 290px;
    display: flex; flex-direction: column; align-items: center; gap: 18px;
  }
  .back-dot {
    width: 62px; height: 62px; border-radius: 50%;
    background: var(--brand-yellow);
  }
  .back-name {
    color: var(--text-grey);
    font-size: 24px; letter-spacing: 1.5px;
  }
  .contact-list {
    position: absolute; left: 36px; top: 190px;
    list-style: none;
    color: var(--text-grey);
    font-size: 25px;
  }
  .contact-item {
    display: flex; align-items: center; gap: 12px;
    height: 37px;
  }
  .contact-icon { width: 24px; height: 24px; flex: none; }
  .contact-pair { gap: 0; }
  .contact-pair .contact-social { display: flex; align-items: center; gap: 12px; }
  .contact-pair .contact-social + .contact-social { margin-left: 48px; }
</style>
</head>
<body>
<main class="canvas">

  <section class="card-front" aria-label="Frente do cartão">
    <div class="front-mark">
      <span class="front-dot"></span>
      <div>
        <p class="front-name">MARINA LACERDA</p>
        <p class="front-tagline">ARQUITETURA • INTERIORES</p>
      </div>
    </div>
  </section>

  <section class="card-back" aria-label="Verso do cartão">
    <svg class="card-back-shape" viewBox="0 0 800 450" width="800" height="450" aria-hidden="true">
      <rect width="800" height="450" fill="var(--card-white)"/>
      <path d="M760 0 C800 180 760 330 620 450 L800 450 L800 0 Z" fill="var(--brand-yellow)"/>
    </svg>

    <div class="back-mark">
      <span class="back-dot"></span>
      <p class="back-name">MARINA LACERDA</p>
    </div>

    <ul class="contact-list">
      <li class="contact-item">
        <svg class="contact-icon" viewBox="0 0 24 24"><circle cx="12" cy="12" r="12" fill="var(--icon-grey)"/><path d="M12 5a4.5 4.5 0 0 0-4.5 4.5C7.5 13 12 18 12 18s4.5-5 4.5-8.5A4.5 4.5 0 0 0 12 5z" fill="#fff"/><circle cx="12" cy="9.5" r="1.6" fill="var(--icon-grey)"/></svg>
        <span>Rua das Acácias 218, sala 4</span>
      </li>
      <li class="contact-item">
        <span class="contact-icon"></span>
        <span>Centro • Vale Claro • Bahia</span>
      </li>
      <li class="contact-item">
        <svg class="contact-icon" viewBox="0 0 24 24"><circle cx="12" cy="12" r="12" fill="var(--icon-grey)"/><path d="M8.5 6.5l2 .2 1 2.6-1.3 1a7 7 0 0 0 3.5 3.5l1-1.3 2.6 1 .2 2c-.4.9-1.4 1.4-2.4 1.3A10 10 0 0 1 7.2 8.9c-.1-1 .4-2 1.3-2.4z" fill="#fff"/></svg>
        <span>(75) 90000-1234 • 90000-5678</span>
      </li>
      <li class="contact-item">
        <svg class="contact-icon" viewBox="0 0 24 24"><circle cx="12" cy="12" r="12" fill="var(--icon-grey)"/><rect x="6" y="8" width="12" height="8.5" rx="1" fill="#fff"/><path d="M6.5 8.6L12 12.8l5.5-4.2" fill="none" stroke="var(--icon-grey)" stroke-width="1.2"/></svg>
        <span>contato@marinalacerda.arq.br</span>
      </li>
      <li class="contact-item">
        <svg class="contact-icon" viewBox="0 0 24 24"><circle cx="12" cy="12" r="12" fill="var(--icon-grey)"/><g fill="none" stroke="#fff" stroke-width="1.2"><circle cx="12" cy="12" r="6"/><ellipse cx="12" cy="12" rx="2.6" ry="6"/><path d="M6 12h12"/></g></svg>
        <span>www.marinalacerda.arq.br</span>
      </li>
      <li class="contact-item contact-pair">
        <span class="contact-social">
          <svg class="contact-icon" viewBox="0 0 24 24"><circle cx="12" cy="12" r="12" fill="var(--icon-grey)"/></svg>
          <span>@marinalacerda.arq</span>
        </span>
        <span class="contact-social">
          <svg class="contact-icon" viewBox="0 0 24 24"><circle cx="12" cy="12" r="12" fill="var(--icon-grey)"/></svg>
          <span>/@marinalacerda.arq</span>
        </span>
      </li>
    </ul>
  </section>

</main>
</body>
</html>
```